organic, healthy living website needs a new home page!

We need a home page for the front page of our website (www.fernmeadowco.com.au).

We want to see the following at a glance! We want to gain trust - communicate value, and navigate visitors to the next step - purchasing!

Our two main products:
- certified organic veggies (weekly in Melbourne, Australia - Mentone, Frankston and Ringwood with more pick up locations to come soon)

-ethical wooden toys (by membership only at this stage - run quarterly as a bulk buy - just for Melbourne people!)

Other products:
- health appliances - juicers, dehydrators and water filters (free delivery to their door all over Australia)

- natural parenting products which promote breastfeeding, homebirth, cosleeping and gentle parenting (books, jewellery, gifts, blessingway etc) all over Australia - send via Southern Parcelway.

This website holds all of our products for purchase. We want to emphasise exactly what is to offer here. We will have an info blog which we want to link THROUGH the product homepage of FM. The blog will include a directory of natural services (for a very niche market), recipes, stories, and a wealth of information to do with natural pregnancy, health, parenting, health and community!

We have 5 images linked below - we need these to correspond with the words PREGNANCY, BIRTH, PARENTING, HEALTH, And COMMUNITY and maybe a little design on these - such as dragonflies or flowers - or both. We will code these to work in a slideshow, and link to our blog.

We want this page to feature everything we do, but also be aesthetically pleasing without overkill. We want it to reflect our style, and vision. Natural, organic, and as close to nature as possible. Flow is important, as is consistency throughout the page. WE want it to appeal to our hippy mamas and papas who just want to love their babies, live organically and as healthy as they can.

We love the look and feel of the following websites:

http://brightlarderhub.com/

Thank you!!

Target Market(s)

20-50 year old parents who are environmentally aware and health conscious. They have very close bonds to their children.
Think bohemian, rustic, vintage yet with a modern feel.

Industry/Entity Type

Health

Font styles to use
Script

Colors
e34197
6b449b
33a6d7
0455a3
33b7a4

Requirements
Must have
• Must be clean and say at a glance exactly what we do.

```html
<!DOCTYPE html>
<html lang="en">
<head>
<meta charset="utf-8">
<title>Fern Meadow Co – Organic, Raw, Wholefoods</title>
<link href="https://fonts.googleapis.com/css2?family=Handlee&family=Montserrat:wght@400;600;700&display=swap" rel="stylesheet">
<style>
:root{
  --pink:#e34197;
  --purple:#6b2c86;
  --purple-deep:#5a2373;
  --blue:#33a6d7;
  --navy:#0f69b4;
  --teal:#33b7a4;
  --canvas:#e8e8e8;
  --bar:#ececec;
  --bar-dark:#a8a8a8;
  --ink:#222;
  --white:#fff;
}
*{margin:0;padding:0;box-sizing:border-box}
html,body{width:1200px;height:900px;overflow:hidden;background:var(--canvas)}
body{font-family:'Handlee',cursive;color:var(--ink)}
.canvas{position:relative;width:1200px;height:900px}
.abs{position:absolute}
.page{position:absolute;left:321px;top:0;width:558px;height:900px;background:var(--white)}

/* hero */
.hero{left:321px;top:0;width:558px;height:218px;
  background:radial-gradient(circle at 65% 40%,#a3452e 0,#7a4a26 22%,transparent 45%),
  radial-gradient(circle at 20% 80%,#b8503a 0,transparent 30%),
  linear-gradient(180deg,#c9c76c 0%,#8e8a3e 45%,#6d6a2a 75%,#8f7f43 100%)}
.hero-shade{left:321px;top:0;width:558px;height:218px;background:rgba(40,30,10,.22)}
.social{top:13px;left:591px;display:flex;gap:2px}
.social span{width:19px;height:19px;border:1.5px solid #fff;border-radius:50%;display:block}
.search{left:697px;top:14px;width:98px;height:19px;background:rgba(255,255,255,.55)}
.search-btn{left:796px;top:14px;width:19px;height:19px;background:var(--blue)}
.tagline{left:321px;top:79px;width:558px;text-align:center;color:#fff;font-size:10px;white-space:nowrap}
.hero-title{left:321px;top:101px;width:558px;text-align:center;color:#fff;font-family:'Montserrat',sans-serif;font-weight:600;font-size:23.5px;letter-spacing:.8px;white-space:nowrap}
.pill{height:22px;width:93px;border-radius:11px;background:var(--pink);color:#fff;font-family:'Montserrat',sans-serif;font-weight:700;font-size:8px;line-height:22px;text-align:center}

/* header */
.brand{left:345px;top:238px;display:flex;align-items:center;gap:6px}
.brand-dot{width:30px;height:30px;border-radius:50%;background:var(--purple)}
.brand-name{font-family:'Montserrat',sans-serif;font-size:14px;color:var(--purple);font-weight:400;white-space:nowrap}
.nav{left:524px;top:251px;font-family:'Montserrat',sans-serif;font-weight:600;font-size:7px;white-space:nowrap}
.nav span{margin:0 3px}
.cart{left:813px;top:218px;width:42px;height:84px}
.cart-label{left:813px;top:261px;width:42px;text-align:center;color:#fff;font-family:'Montserrat',sans-serif;font-size:7.5px;line-height:13px}

/* journey band */
.journey{left:321px;top:288px;width:558px;height:149px;background:var(--purple)}
.bubble{border-radius:50%;border:4px solid var(--purple-deep);box-shadow:0 0 0 1px rgba(255,255,255,.15)}
.step{width:100px;text-align:center;color:#fff;font-size:13px;line-height:14px}
.step i{display:block;font-style:normal;font-size:9px;letter-spacing:1px;line-height:8px}

/* products */
.tag{height:14px;background:var(--pink);color:#fff;font-family:'Montserrat',sans-serif;font-weight:700;font-size:7px;line-height:14px;padding:0 5px;white-space:nowrap}
.rail{height:14px;background:var(--bar)}
.card{width:120px;height:164px}
.card-photo{width:120px;height:144px}
.card-cap{position:absolute;left:0;top:103px;width:120px;height:14px;background:rgba(255,255,255,.55);color:var(--pink);font-size:8px;text-align:center;line-height:14px;white-space:nowrap}
.card-btn{position:absolute;left:0;top:145px;width:120px;height:19px;background:var(--purple);color:#fff;font-family:'Montserrat',sans-serif;font-weight:600;font-size:7.5px;text-align:center;line-height:19px}
.card-dim{position:absolute;left:0;top:0;width:120px;height:144px;background:rgba(40,40,40,.72)}
.card-title{position:absolute;left:0;top:14px;width:120px;text-align:center;color:#fff;font-family:'Montserrat',sans-serif;font-weight:700;font-size:7px}
.card-note{position:absolute;left:17px;top:35px;width:86px;height:70px;background:rgba(20,20,20,.6);border:1px solid rgba(255,255,255,.25);color:#fff;font-size:6.5px;line-height:13px;padding:8px 4px 0}

/* testimonials */
.arrow{width:14px;height:15px;background:var(--teal)}
.quote{left:398px;top:677px;width:275px;text-align:center;font-size:8px;line-height:12.3px}
.blog{left:735px;top:651px;width:120px;height:91px;background:linear-gradient(90deg,#2b2725 0 42%,#c99a76 60%,#e6cbb1 100%)}
.blog h3{position:absolute;left:8px;top:7px;color:#fff;font-family:'Montserrat',sans-serif;font-size:11px}
.blog ul{position:absolute;left:9px;top:25px;list-style:none;color:#fff;font-size:6px;line-height:8.2px}
.blog .more{position:absolute;right:4px;bottom:3px;background:#fff;color:#222;font-size:6px;padding:0 3px;border-radius:5px}

/* newsletter */
.newsletter{left:317px;top:750px;width:562px;height:33px;background:var(--navy)}
.news-title{left:354px;top:760px;color:#fff;font-family:'Montserrat',sans-serif;font-weight:700;font-size:10.5px;white-space:nowrap}
.news-copy{left:475px;top:758px;color:#fff;font-size:7.5px;line-height:9.5px;white-space:nowrap}
.news-field{left:613px;top:758px;width:156px;height:17px;background:#fff;font-size:6px;color:#999;line-height:17px;padding-left:6px}
.news-btn{left:776px;top:758px;width:66px;height:16px;background:var(--blue);color:#fff;font-size:8px;text-align:center;line-height:16px}

/* footer */
.foot-col{width:119px}
.foot-col h4{height:13px;background:var(--bar);font-family:'Montserrat',sans-serif;font-weight:400;font-size:6.5px;color:#fff;white-space:nowrap;overflow:hidden}
.foot-col h4 span{display:inline-block;background:var(--bar-dark);padding:0 3px;line-height:13px;min-width:52px;white-space:nowrap}
.foot-col p{font-size:6.5px;line-height:13px;margin-top:2px;padding-left:1px;white-space:nowrap}
.foot-col p+p{margin-top:0}
.social-links{left:321px;top:843px;width:558px;text-align:center;font-size:6.5px;white-space:nowrap}
.social-links b{display:inline-block;width:7px;height:9px;background:var(--navy);vertical-align:middle;margin-right:4px}
.rule{left:350px;top:856px;width:486px;height:1px;background:linear-gradient(90deg,transparent,#3a78c0,transparent)}
.copyright{left:347px;top:866px;font-size:6.5px;white-space:nowrap}
.copyright em{font-style:normal;color:var(--navy)}
.payments{left:729px;top:862px;display:flex;gap:4px}
.payments span{width:22px;height:15px;border:1px solid #c8c8c8;background:#f4f4f4}
</style>
</head>
<body>
<div class="canvas">
  <div class="page"></div>

  <!-- hero -->
  <div class="abs hero" role="img" aria-label="Red apples in a woven basket on sunlit grass"></div>
  <div class="abs hero-shade"></div>
  <div class="abs social" aria-label="Social links"><span></span><span></span><span></span><span></span><span></span></div>
  <div class="abs search"></div>
  <div class="abs search-btn">
    <svg width="19" height="19" viewBox="0 0 19 19"><circle cx="8.5" cy="8.5" r="3.6" fill="none" stroke="#fff" stroke-width="1.6"/><line x1="11" y1="11" x2="14" y2="14" stroke="#fff" stroke-width="1.8"/></svg>
  </div>
  <svg class="abs" style="left:828px;top:16px" width="13" height="15" viewBox="0 0 13 15"><circle cx="6.5" cy="4" r="3.2" fill="#fff"/><path d="M1 15v-3.5c0-2 2-3.5 5.5-3.5s5.5 1.5 5.5 3.5V15z" fill="#fff"/></svg>
  <p class="abs tagline">Organic produce sourced from local and interstate farmers delivered direct to your local pickup location</p>
  <h1 class="abs hero-title">ORGANIC - RAW - WHOLEFOODS</h1>
  <div class="abs pill" style="left:489px;top:145px">SHOP NOW</div>
  <div class="abs pill" style="left:617px;top:145px">RECOMMENDED</div>

  <!-- header -->
  <div class="abs brand"><span class="brand-dot"></span><span class="brand-name">Fern Meadow Co</span></div>
  <nav class="abs nav">ABOUT US<span>|</span>SHOP<span>|</span>DIRECTORY<span>|</span>MEMBERS<span>|</span>BLOG<span>|</span>RECOMMENDED</nav>
  <svg class="abs cart" viewBox="0 0 42 84"><path d="M0 0H42V84L21 74L0 84Z" fill="#e34197"/><circle cx="21" cy="24" r="11" fill="#6b2c86"/><path d="M15 22h12l-1.5 7h-9z" fill="none" stroke="#fff" stroke-width="1.3"/><path d="M17 22l4-5 4 5" fill="none" stroke="#fff" stroke-width="1.3"/></svg>
  <div class="abs cart-label">CART<br>$0.00</div>

  <!-- journey -->
  <div class="abs journey"></div>
  <svg class="abs" style="left:321px;top:288px" width="558" height="149" viewBox="0 0 558 149">
    <path d="M85 40 C120 20 110 70 140 68 M200 58 C220 40 230 10 245 40 M280 70 C300 100 330 90 360 88 M420 70 C440 60 450 20 470 40" fill="none" stroke="#fff" stroke-width="1.2" stroke-dasharray="4 3"/>
  </svg>
  <div class="abs bubble" style="left:346px;top:305px;width:64px;height:64px;background:#c9a38a" role="img" aria-label="Pregnant belly with a bead necklace"></div>
  <div class="abs bubble" style="left:459px;top:324px;width:64px;height:64px;background:#8a8a8a" role="img" aria-label="Black and white birth moment"></div>
  <div class="abs bubble" style="left:568px;top:312px;width:64px;height:64px;background:linear-gradient(#e2a86a,#c98a4f)" role="img" aria-label="Family walking on a beach at sunset"></div>
  <div class="abs bubble" style="left:682px;top:331px;width:64px;height:64px;background:#e6d7c2" role="img" aria-label="Hands joined in a circle"></div>
  <div class="abs bubble" style="left:788px;top:314px;width:64px;height:64px;background:linear-gradient(135deg,#7fae3f,#d8562b)" role="img" aria-label="Fresh fruit and vegetables"></div>
  <div class="abs step" style="left:330px;top:403px">Pregnancy<i>•••</i></div>
  <div class="abs step" style="left:442px;top:403px">Birth<i>•••</i></div>
  <div class="abs step" style="left:547px;top:403px">Parenting<i>•••</i></div>
  <div class="abs step" style="left:662px;top:403px">Community<i>•••</i></div>
  <div class="abs step" style="left:772px;top:403px">Health<i>•••</i></div>

  <!-- products -->
  <div class="abs rail" style="left:345px;top:446px;width:250px"></div>
  <div class="abs rail" style="left:605px;top:446px;width:250px"></div>
  <div class="abs tag" style="left:345px;top:446px">MAIN PRODUCTS</div>
  <div class="abs tag" style="left:605px;top:446px">OTHER PRODUCTS</div>
  <div class="abs" style="left:599px;top:446px;width:1px;height:188px;background:#888"></div>
  <div class="abs" style="left:596px;top:462px;width:7px;height:7px;border:1px solid var(--pink);border-radius:50%;background:#fff"></div>

  <div class="abs card" style="left:345px;top:470px">
    <div class="card-photo" style="background:linear-gradient(160deg,#3f6b2c,#c57a3b 60%,#d9c6a5)" role="img" aria-label="Crate of organic vegetables"></div>
    <div class="card-cap">CERTIFIED ORGANIC VEGGIES</div>
    <div class="card-btn">GO TO SHOP</div>
  </div>
  <div class="abs card" style="left:475px;top:470px">
    <div class="card-photo" style="background:#8a7a6a" role="img" aria-label="Wooden toys"></div>
    <div class="card-dim"></div>
    <div class="card-title">ETHICAL WOODEN TOYS</div>
    <div class="card-note">by membership only at this stage run quarterly as a bulk buy just for Melbourne people!</div>
    <svg style="position:absolute;left:50px;top:113px" width="20" height="20" viewBox="0 0 20 20"><circle cx="10" cy="10" r="9" fill="none" stroke="#fff" stroke-width="1.2"/><path d="M5 9h10l-1.4 5H6.4z" fill="none" stroke="#fff" stroke-width="1.1"/></svg>
    <div class="card-btn">GO TO SHOP</div>
  </div>
  <div class="abs card" style="left:605px;top:470px">
    <div class="card-photo" style="background:linear-gradient(180deg,#eef0ef,#c9d4d8 70%,#6aa04a)" role="img" aria-label="Woman juicing in a kitchen"></div>
    <div class="card-cap">HEALTH APPLIANCES</div>
    <div class="card-btn">GO TO SHOP</div>
  </div>
  <div class="abs card" style="left:735px;top:470px">
    <div class="card-photo" style="background:linear-gradient(180deg,#a9c46a,#d8b79a 60%,#c9607a)" role="img" aria-label="Mother and children on a picnic blanket"></div>
    <div class="card-cap">NATURAL PARENTING</div>
    <div class="card-btn">GO TO SHOP</div>
  </div>

  <!-- testimonials -->
  <div class="abs rail" style="left:345px;top:651px;width:377px"></div>
  <div class="abs tag" style="left:476px;top:651px;width:116px;text-align:center;font-size:8px">TESTIMONIALS</div>
  <svg class="abs arrow" style="left:350px;top:688px" viewBox="0 0 14 15"><rect width="14" height="15" fill="#33b7a4"/><path d="M8.5 4L5 7.5 8.5 11" fill="none" stroke="#fff" stroke-width="1.6"/></svg>
  <svg class="abs arrow" style="left:704px;top:688px" viewBox="0 0 14 15"><rect width="14" height="15" fill="#33b7a4"/><path d="M5.5 4L9 7.5 5.5 11" fill="none" stroke="#fff" stroke-width="1.6"/></svg>
  <p class="abs quote">I recently purchased a wooden butterfly puzzle from Fern Meadow Co for my 28 and 15 month old daughters. It has become one of their favourite toys and is very easy to use for their little hands, both of my girls love playing for hours with this great and colourful wooden toy!</p>
  <svg class="abs" style="left:518px;top:727px" width="34" height="8" viewBox="0 0 34 8"><g fill="none" stroke-width="1"><circle cx="4" cy="4" r="2.6" stroke="#e34197"/><circle cx="12" cy="4" r="2.6" stroke="#aaa"/><circle cx="20" cy="4" r="2.6" stroke="#aaa"/><circle cx="28" cy="4" r="2.6" stroke="#aaa"/></g></svg>
  <div class="abs blog" role="img" aria-label="Bowl of brown eggs">
    <h3>BLOG</h3>
    <ul><li>recipes</li><li>stories</li><li>natural pregnancy</li><li>health</li><li>parenting</li><li>health</li><li>community</li></ul>
    <span class="more">and much more! ▸</span>
  </div>

  <!-- newsletter -->
  <div class="abs newsletter"></div>
  <div class="abs news-title">STAY CONNECTED</div>
  <p class="abs news-copy">Enter your email address to receive<br>special offers and promotions.</p>
  <div class="abs news-field">Enter e-mail address</div>
  <div class="abs news-btn">subscribe</div>

  <!-- footer -->
  <div class="abs foot-col" style="left:345px;top:788px"><h4><span>MY ACCOUNT</span></h4><p>Sign in</p><p>Create account</p></div>
  <div class="abs foot-col" style="left:477px;top:788px"><h4><span>OUR STORE</span></h4><p>Contact us</p><p>Sitemap</p></div>
  <div class="abs foot-col" style="left:605px;top:788px"><h4><span>CUSTOMER SERVICE</span></h4><p>About your order</p></div>
  <div class="abs foot-col" style="left:735px;top:788px"><h4><span>ABOUT FERN MEADOW CO</span></h4><p>Sign in</p><p>Create account</p></div>
  <div class="abs social-links"><b></b>Fern Meadow Co on Friendsphere &nbsp; | &nbsp; <b></b>Melbourne Members on Friendsphere</div>
  <div class="abs rule"></div>
  <p class="abs copyright">© 2004–2014 <em>Fern Meadow Co</em>. Powered by Earth loving Hippies like you!</p>
  <div class="abs payments" aria-label="Accepted payment methods"><span></span><span></span><span></span><span></span><span></span></div>
</div>
</body>
</html>
```